Pregnancy and Fertility Information Website

Hello Designers,
I need a website which provide tips and information about healthy and happy pregnancy. My website name is Lorvin medical.

The website should provide all the information needed throughout pregnancy and beyond ranging from pregnancy tracking tools and articles about common pregnancy concerns and what to expect during pregnancy,etc.
The details about first trimester, second trimester and third trimester should be highlighted in the website.

Top Navigation
Home, Fertility, Pregnancy basics, Articles, Tips and News

I'm looking for a simple and clean design which involves captivating images and colors but it shouldn't be crowded. The design must be professional and modern. An easy to navigate layout is a must.

Green, violet, blue and light yellow colors are my favorites but i'm open to other options.

Any questions. Kindly ask

Industry/Entity Type

Medical

```html
<!DOCTYPE html>
<html lang="en">
<head>
<meta charset="utf-8">
<title>Lorvin Medical</title>
<link rel="stylesheet" href="https://fonts.googleapis.com/css2?family=Montserrat:wght@400;600;700;800&family=Open+Sans:wght@400;700&display=swap">
<style>
:root{
  --cyan:#10f0f0;
  --cyan-deep:#19d6dc;
  --green:#22cc66;
  --green-text:#3ce07a;
  --grey-title:#7a7a7a;
  --ink:#333333;
  --paper:#ffffff;
  --mist:#f2f2f2;
  --footer:#242424;
}
*{box-sizing:border-box;margin:0;padding:0}
html,body{width:1200px;height:2400px;overflow:hidden;background:var(--paper)}
body{position:relative;font-family:"Open Sans",Arial,sans-serif;color:var(--ink)}
.abs{position:absolute}

/* hero */
.hero{left:0;top:0;width:1200px;height:600px;background:linear-gradient(100deg,#8a8178 0%,#6f6a63 35%,#7c8070 70%,#8d9184 100%)}
.hero-photo{left:0;top:0;width:1200px;height:600px;background:radial-gradient(ellipse at 25% 45%,rgba(205,190,175,.55),rgba(0,0,0,0) 55%)}
.brand{left:56px;top:16px;display:flex;align-items:center;gap:16px}
.brand-mark{width:70px;height:70px;border-radius:50%;background:#2b7fc4}
.brand-name{font-family:"Montserrat",sans-serif;font-weight:700;font-size:18px;color:var(--green-text);letter-spacing:2px;line-height:30px;width:110px}
.nav{top:76px;left:392px;display:flex;font-family:"Montserrat",sans-serif;font-weight:700;font-size:16px;letter-spacing:2px;color:#fff}
.nav a{color:#fff;text-decoration:none;position:absolute;white-space:nowrap}
.nav a.active{color:var(--green-text)}
.social{top:14px;left:1068px;display:flex;gap:14px}
.social span{width:30px;height:30px;border-radius:50%;display:block}
.hero-title{left:0;width:1200px;top:274px;text-align:center;font-family:"Montserrat",sans-serif;font-weight:400;font-size:34px;letter-spacing:5px;color:#fff}
.hero-btn{left:490px;top:342px;width:232px;height:55px;border:2px solid #fff;color:#fff;font-size:17px;display:flex;align-items:center;justify-content:center;letter-spacing:1px}
.slide-arrow{top:292px;width:30px;height:30px;border-radius:50%;background:rgba(255,255,255,.75)}

/* section titles */
.section-title{left:0;width:1200px;text-align:center;font-family:"Montserrat",sans-serif;font-weight:700;font-size:29px;letter-spacing:9px;line-height:42px}
.title-grey{color:var(--grey-title)}
.title-white{color:#fff}

/* cards */
.card{overflow:hidden}
.card-frame{position:absolute;left:10px;top:10px;right:10px;bottom:10px;border:2px solid var(--cyan-deep)}
.card-label{position:absolute;font-family:"Montserrat",sans-serif;font-weight:800;font-size:21px;letter-spacing:6px;color:#fff;line-height:30px}
.card-more{position:absolute;right:20px;bottom:16px;display:flex;align-items:center;gap:6px;font-family:"Montserrat",sans-serif;font-weight:700;font-size:10px;color:var(--cyan-deep)}
.photo-phone{background:linear-gradient(135deg,#6f5a4a,#c9c4bd 45%,#8a6a55)}
.photo-hands{background:linear-gradient(160deg,#5a2a22,#b86b55 50%,#3c1d19)}
.photo-belly{background:linear-gradient(120deg,#9aa0a0,#2d2d35 50%,#a8a59c)}

/* phases */
.phases{left:0;top:1187px;width:1200px;height:573px;background:linear-gradient(120deg,#22e4ea,#12f0f2 55%,#2fdbe0)}

/* memories */
.memories{left:0;top:1760px;width:1200px;height:600px;background:var(--mist)}
.memory-panel{left:88px;top:1878px;width:1022px;height:482px;background:var(--paper)}
.memory-head{left:88px;top:1878px;width:1022px;height:52px;background:var(--cyan);font-family:"Montserrat",sans-serif;font-weight:700;font-size:20px;color:#fff;letter-spacing:1px}
.memory-head span{position:absolute;top:13px}
.memory-row{left:0;width:1200px;height:40px;font-size:13px;font-weight:700;color:var(--ink)}
.memory-row span{position:absolute;top:0}
.memory-row small{display:block;font-size:7px;font-weight:400;letter-spacing:.5px;margin-top:2px}
.btn{top:2278px;height:37px;width:150px;display:flex;align-items:center;justify-content:center;font-family:"Montserrat",sans-serif;font-weight:700;font-size:14px;color:#fff;letter-spacing:1px}
.btn-green{left:424px;background:var(--green)}
.btn-cyan{left:624px;background:var(--cyan)}

.footer{left:0;top:2360px;width:1200px;height:40px;background:var(--footer);color:var(--green-text);font-family:"Montserrat",sans-serif;font-weight:700;font-size:14px;letter-spacing:1px;display:flex;align-items:center;justify-content:center}
</style>
</head>
<body>

<header>
  <div class="abs hero" role="img" aria-label="Photo of a pregnant woman sitting by a bright window"></div>
  <div class="abs hero-photo"></div>
  <div class="abs brand"><span class="brand-mark"></span><span class="brand-name">LORVIN MEDICAL</span></div>
  <nav class="abs nav">
    <a class="active" style="left:0">HOME</a>
    <a style="left:104px">FERTILITY</a>
    <a style="left:242px">PREGNANCY BASICS</a>
    <a style="left:467px">ARTICLES</a>
    <a style="left:603px">TIPS&amp;NEWS</a>
  </nav>
  <div class="abs social" aria-label="Social links">
    <span style="background:#3b5998"></span>
    <span style="background:#8a8a8a"></span>
    <span style="background:#dd4b39"></span>
  </div>
  <svg class="abs slide-arrow" style="left:28px" viewBox="0 0 30 30"><path d="M17 9l-6 6 6 6" fill="none" stroke="#555" stroke-width="2.5"/></svg>
  <svg class="abs slide-arrow" style="left:1150px" viewBox="0 0 30 30"><path d="M13 9l6 6-6 6" fill="none" stroke="#555" stroke-width="2.5"/></svg>
  <h1 class="abs hero-title">GOING THROUGH PREGNANCY</h1>
  <div class="abs hero-btn">VIEW TIPS</div>
</header>

<section>
  <h2 class="abs section-title title-grey" style="top:658px">THINGS YOU SHOULD<br>KNOW</h2>

  <div class="abs card photo-phone" style="left:88px;top:787px;width:291px;height:285px" role="img" aria-label="Hand holding a phone with a pregnancy tracking app">
    <div class="card-frame"></div>
    <div class="card-label" style="left:22px;bottom:22px">TRACKING<br>TOOLS</div>
    <div class="card-more"><svg width="18" height="18" viewBox="0 0 18 18"><circle cx="9" cy="9" r="9" fill="#19d6dc"/><path d="M7 5l4 4-4 4" fill="none" stroke="#222" stroke-width="2"/></svg>KNOW MORE</div>
  </div>
  <div class="abs card photo-hands" style="left:394px;top:787px;width:408px;height:285px" role="img" aria-label="Hands forming a heart on a pregnant belly">
    <div class="card-frame"></div>
    <div class="card-label" style="left:26px;bottom:22px">WHAT TO<br>EXPECT?</div>
    <div class="card-more"><svg width="18" height="18" viewBox="0 0 18 18"><circle cx="9" cy="9" r="9" fill="#19d6dc"/><path d="M7 5l4 4-4 4" fill="none" stroke="#222" stroke-width="2"/></svg>KNOW MORE</div>
  </div>
  <div class="abs card photo-belly" style="left:818px;top:787px;width:292px;height:285px" role="img" aria-label="Pregnant woman holding her back in a living room">
    <div class="card-frame"></div>
    <div class="card-label" style="left:22px;bottom:22px">PREGNANCY<br>CONCERN</div>
    <div class="card-more"><svg width="18" height="18" viewBox="0 0 18 18"><circle cx="9" cy="9" r="9" fill="#19d6dc"/><path d="M7 5l4 4-4 4" fill="none" stroke="#222" stroke-width="2"/></svg>KNOW MORE</div>
  </div>
</section>

<section>
  <div class="abs phases" role="img" aria-label="Cyan tinted photo of a woman in a home interior"></div>
  <h2 class="abs section-title title-white" style="top:1247px;line-height:32px">DIFFERENT PHASES OF<br>PREGNANCY</h2>

  <div class="abs card photo-phone" style="left:91px;top:1379px;width:290px;height:285px" role="img" aria-label="Hand holding a phone with a pregnancy tracking app">
    <div class="card-frame"></div>
    <div class="card-label" style="left:0;right:0;top:110px;text-align:center">FIRST<br>TRIMESTER</div>
    <div class="card-more"><svg width="18" height="18" viewBox="0 0 18 18"><circle cx="9" cy="9" r="9" fill="#19d6dc"/><path d="M7 5l4 4-4 4" fill="none" stroke="#222" stroke-width="2"/></svg>KNOW MORE</div>
  </div>
  <div class="abs card photo-hands" style="left:395px;top:1379px;width:410px;height:285px" role="img" aria-label="Hands forming a heart on a pregnant belly">
    <div class="card-frame"></div>
    <div class="card-label" style="left:0;right:0;top:110px;text-align:center">SECOND<br>TRIMESTER</div>
    <div class="card-more"><svg width="18" height="18" viewBox="0 0 18 18"><circle cx="9" cy="9" r="9" fill="#19d6dc"/><path d="M7 5l4 4-4 4" fill="none" stroke="#222" stroke-width="2"/></svg>KNOW MORE</div>
  </div>
  <div class="abs card photo-belly" style="left:819px;top:1379px;width:291px;height:285px" role="img" aria-label="Pregnant woman holding her back in a living room">
    <div class="card-frame"></div>
    <div class="card-label" style="left:0;right:0;top:110px;text-align:center">THIRD<br>TRIMESTER</div>
    <div class="card-more"><svg width="18" height="18" viewBox="0 0 18 18"><circle cx="9" cy="9" r="9" fill="#19d6dc"/><path d="M7 5l4 4-4 4" fill="none" stroke="#222" stroke-width="2"/></svg>KNOW MORE</div>
  </div>
</section>

<section>
  <div class="abs memories"></div>
  <h2 class="abs section-title title-grey" style="top:1800px;letter-spacing:5px">MEMORIES</h2>
  <div class="abs memory-panel"></div>
  <div class="abs memory-head"><span style="left:10px">MEMORY</span><span style="left:514px">POSTED BY</span><span style="left:882px">POSTED ON</span></div>

  <div class="abs memory-row" style="top:1946px"><span style="left:98px">FIRST MONTH<small>A SHORT NOTE ABOUT OUR FIRST MONTH</small></span><span style="left:602px">RACHEL</span><span style="left:970px;font-weight:400">01/04/2017</span></div>
  <div class="abs memory-row" style="top:1995px"><span style="left:98px">FIRST MONTH<small>A SHORT NOTE ABOUT OUR FIRST MONTH</small></span><span style="left:602px">RACHEL</span><span style="left:970px;font-weight:400">01/04/2017</span></div>
  <div class="abs memory-row" style="top:2044px"><span style="left:98px">FIRST MONTH<small>A SHORT NOTE ABOUT OUR FIRST MONTH</small></span><span style="left:602px">RACHEL</span><span style="left:970px;font-weight:400">01/04/2017</span></div>
  <div class="abs memory-row" style="top:2093px"><span style="left:98px">FIRST MONTH<small>A SHORT NOTE ABOUT OUR FIRST MONTH</small></span><span style="left:602px">RACHEL</span><span style="left:970px;font-weight:400">01/04/2017</span></div>
  <div class="abs memory-row" style="top:2142px"><span style="left:98px">FIRST MONTH<small>A SHORT NOTE ABOUT OUR FIRST MONTH</small></span><span style="left:602px">RACHEL</span><span style="left:970px;font-weight:400">01/04/2017</span></div>
  <div class="abs memory-row" style="top:2191px"><span style="left:98px">FIRST MONTH<small>A SHORT NOTE ABOUT OUR FIRST MONTH</small></span><span style="left:602px">RACHEL</span><span style="left:970px;font-weight:400">01/04/2017</span></div>

  <div class="abs btn btn-green">VIEW ALL</div>
  <div class="abs btn btn-cyan">TELL YOURS</div>
</section>

<footer class="abs footer">COPYRIGHT © 2017 LORVIN MEDICAL</footer>

</body>
</html>
```